I would like a stylish low key card that represents my Cedar Nook. A boutique rental property . This property is of the highest standard and I wish the card to covey this without being old fashion

Boutique

Tessa Varrow
0427350192
tessa.varrow@varrow.com.au Cedar Nook

```html
<!DOCTYPE html>
<html lang="en">
<head>
<meta charset="utf-8">
<title>The Cedar Nook – Tessa Varrow</title>
<link rel="stylesheet" href="https://fonts.googleapis.com/css2?family=Abril+Fatface&family=PT+Serif&display=swap">
<style>
  :root {
    --paper: #ffffff;
    --band: #1d1d1d;
    --ink: #151515;
    --sage: #bcbb98;
  }
  html, body {
    margin: 0;
    padding: 0;
    width: 1200px;
    height: 693px;
    overflow: hidden;
    background: var(--paper);
  }
  .card {
    position: relative;
    width: 1200px;
    height: 693px;
    background: var(--paper);
  }
  .rule {
    position: absolute;
    left: 0;
    width: 1200px;
    height: 19px;
    background: var(--band);
  }
  .rule--top { top: 113px; }
  .rule--bottom { top: 383px; }
  .banner {
    position: absolute;
    left: 0;
    top: 143px;
    width: 1200px;
    height: 226px;
    background: var(--band);
    display: flex;
    align-items: center;
    justify-content: center;
  }
  .brand-name {
    margin: 0;
    font-family: "PT Serif", serif;
    font-weight: 400;
    font-size: 112px;
    letter-spacing: 4px;
    color: var(--sage);
    line-height: 1;
    padding-top: 20px;
  }
  .contact {
    position: absolute;
    left: 64px;
    top: 420px;
    color: var(--ink);
  }
  .contact__name {
    margin: 0;
    font-family: "Abril Fatface", serif;
    font-weight: 400;
    font-size: 54px;
    line-height: 60px;
    letter-spacing: -0.5px;
  }
  .contact__line {
    margin: 0;
    font-family: "PT Serif", serif;
    font-size: 45px;
    line-height: 56px;
  }
</style>
</head>
<body>
  <main class="card">
    <div class="rule rule--top"></div>
    <header class="banner">
      <h1 class="brand-name">The Cedar Nook</h1>
    </header>
    <div class="rule rule--bottom"></div>
    <section class="contact">
      <p class="contact__name">Tessa Varrow</p>
      <p class="contact__line">tel: 0427350192</p>
      <p class="contact__line">tessa.varrow@varrow.com.au</p>
    </section>
  </main>
</body>
</html>
```